RM Tomás Rivera (Business Card)

Hi designers, in this work, I'm looking for an sophisticated stylish, elegant and proffesional personal card. We have a laboratory of pathology automated, with equipments high quality.
In this web the designers, have created my business logo, the name is "RM Tomás Rivera"
In our lab, we principal work is to prepare the biopsies for further diagnostic of diseases like cancer, tumors, etc.
I need that the first face, only having my complete logo (Rm Tomás Rivera, Laboratorio de procesamiento Histologico)
The overleaf, could repeat the same logo, like water logo.
In this face, I need to say: My full data:

Técnico en Anatomía Patológica
Tomás Rivera Ibarra M.P 47203
Av. Paredes Luján 418 - 2do piso - Instituto Marbel.
Córdoba, Argentina
(0351) 154820937
rivera.tomas@correolab.example

with respect the colors of card, use your imagination, the original logo color is violet, I haven't chosen a color base for the card.

attached pictures are examples of cards I like your DESIGN.
Attached too, the original logo to my company.

the size of card are:
horizontal: 9cm
vertical: 5,5cm

any question that you have, not doubt to question me,
Hand to work!

Industry/Entity Type

Laboratory

Requirements
Must have
• designers sophisticated, not simples, like show the images attached

```html
<!DOCTYPE html>
<html lang="es">
<head>
<meta charset="utf-8">
<title>Tomás Rivera – Tarjeta personal</title>
<link rel="stylesheet" href="https://fonts.googleapis.com/css2?family=Roboto+Condensed:wght@300;400;700&display=swap">
<style>
  :root {
    --backdrop: #efedee;
    --card-black: #0b0b0b;
    --card-white: #ffffff;
    --violet: #8c46c8;
    --violet-light: #a865dd;
    --violet-deep: #6f2fa8;
    --grey-text: #8a8a8a;
    --grey-dark: #5c5c5c;
    --silver: #c9c9c9;
    --white: #ffffff;
  }
  * { box-sizing: border-box; margin: 0; padding: 0; }
  html, body { width: 1200px; height: 800px; overflow: hidden; }
  body {
    background: var(--backdrop);
    font-family: "Roboto Condensed", "Arial Narrow", sans-serif;
    position: relative;
  }
  .card {
    position: absolute;
    top: 247px;
    width: 500px;
    height: 306px;
    border-radius: 4px;
    overflow: hidden;
    box-shadow: 0 6px 18px rgba(0,0,0,0.18);
  }
  .card--front { left: 70px; background: var(--card-black); }
  .card--back { left: 630px; background: var(--card-white); }
  .card__art { position: absolute; inset: 0; width: 100%; height: 100%; }

  .brand { display: flex; align-items: center; gap: 10px; }
  .brand__mark { background: var(--violet); flex: none; }
  .brand__name { color: var(--silver); font-weight: 300; letter-spacing: 0.08em; white-space: nowrap; }
  .brand__tagline {
    color: var(--grey-text); font-weight: 300;
    text-transform: uppercase; white-space: nowrap;
  }

  /* front lockup: name and tagline slanted together */
  .lockup {
    position: absolute; left: 46px; top: 96px; width: 410px;
    display: flex; flex-direction: column; align-items: center; gap: 6px;
    transform: rotate(-6deg); transform-origin: center;
  }
  .lockup .brand__mark { width: 24px; height: 24px; }
  .lockup .brand__name { font-size: 28px; }
  .lockup .brand__tagline { font-size: 19px; letter-spacing: 0; }

  .card--back .brand { position: absolute; left: 50%; top: 26px; transform: translateX(-50%); gap: 6px; }
  .card--back .brand__mark { width: 13px; height: 13px; }
  .card--back .brand__name { font-size: 15px; color: var(--grey-dark); }
  .card--back .brand__tagline { position: absolute; left: 50%; top: 50px; transform: translateX(-50%); font-size: 9px; color: var(--grey-dark); }

  .identity { position: absolute; left: 0; right: 0; top: 72px; text-align: center; }
  .identity__role { color: var(--violet); font-weight: 700; font-size: 14px; }
  .identity__name { color: var(--grey-dark); font-weight: 700; font-size: 27px; line-height: 1.05; }
  .identity__licence { color: var(--grey-text); font-size: 12px; letter-spacing: 0.05em; }

  .contact {
    position: absolute; right: 22px; top: 170px; text-align: right; font-style: normal;
    color: var(--white); font-size: 13px; line-height: 1.75;
  }
  .address {
    position: absolute; left: 22px; top: 234px; font-style: normal;
    color: var(--white); font-size: 12px; font-weight: 700; line-height: 1.6;
  }
</style>
</head>
<body>

<section class="card card--front" aria-label="Frente de la tarjeta">
  <svg class="card__art" viewBox="0 0 500 306" preserveAspectRatio="none" aria-hidden="true">
    <defs>
      <linearGradient id="sheen" x1="0" y1="0" x2="1" y2="0">
        <stop offset="0" stop-color="#9a9a9a"/>
        <stop offset="0.5" stop-color="#ffffff"/>
        <stop offset="1" stop-color="#bdbdbd"/>
      </linearGradient>
    </defs>
    <path d="M0 240 C150 252 330 216 500 160 L500 306 L0 306 Z" fill="var(--violet)"/>
    <path d="M0 230 C150 242 330 204 500 148 L500 160 C330 216 150 252 0 240 Z" fill="url(#sheen)"/>
    <path d="M0 284 C190 290 360 272 500 246" fill="none" stroke="var(--white)" stroke-width="2" opacity="0.9"/>
    <path d="M0 294 C190 300 360 284 500 258 L500 306 L0 306 Z" fill="var(--violet-deep)" opacity="0.5"/>
  </svg>
  <div class="lockup">
    <div class="brand">
      <span class="brand__mark"></span>
      <span class="brand__name">RM Tomás Rivera</span>
    </div>
    <p class="brand__tagline">Laboratorio de procesamiento histologico</p>
  </div>
</section>

<section class="card card--back" aria-label="Dorso de la tarjeta">
  <svg class="card__art" viewBox="0 0 500 306" preserveAspectRatio="none" aria-hidden="true">
    <path d="M0 200 C150 214 320 178 500 118 L500 306 L0 306 Z" fill="var(--violet)"/>
    <path d="M0 212 C170 226 330 196 500 140 L500 172 C330 226 170 246 0 236 Z" fill="var(--violet-light)" opacity="0.55"/>
    <path d="M0 196 C150 210 320 174 500 114" fill="none" stroke="#e2e2e2" stroke-width="2"/>
  </svg>
  <div class="brand">
    <span class="brand__mark"></span>
    <span class="brand__name">RM Tomás Rivera</span>
  </div>
  <p class="brand__tagline">Laboratorio de procesamiento histologico</p>

  <div class="identity">
    <p class="identity__role">Técnico en Anatomía Patológica</p>
    <h1 class="identity__name">Tomás Rivera Ibarra</h1>
    <p class="identity__licence">M.P 47203</p>
  </div>

  <address class="contact">
    (0351) 154820937<br>
    rivera.tomas@correolab.example
  </address>

  <address class="address">
    Av. Paredes Luján 418<br>
    2do piso - Instituto Marbel<br>
    Córdoba, Argentina
  </address>
</section>

</body>
</html>
```